Chill Bo
frozen yogurt and more
Corporate
Tara Kessler
Owner
4182 Larkspur Ln.
Columbus IN. 47358
tarasglow@quillpost.com
Don't have store open yet so have no address or phone numbers. We want logo font the same but would like a standard clean font for the rest of the info

```html
<!DOCTYPE html>
<html lang="en">
<head>
<meta charset="utf-8">
<title>Chill Bo — Stationery Set</title>
<link href="https://fonts.googleapis.com/css2?family=Lato:wght@400;700&display=swap" rel="stylesheet">
<style>
  :root{
    --backdrop:#efebe4;
    --paper:#ffffff;
    --cocoa:#5b3720;
    --cocoa-dark:#4a2c18;
    --lime:#8cc63f;
    --berry:#d9534f;
    --ink:#6b5a4e;
    --soft-ink:#9a8c80;
  }
  *{box-sizing:border-box;margin:0;padding:0}
  html,body{width:1200px;height:432px;overflow:hidden}
  body{background:var(--backdrop);font-family:"Lato",Arial,sans-serif;color:var(--ink);position:relative}

  .brand{display:flex;flex-direction:column;align-items:center;line-height:1}
  .brand-row{display:flex;align-items:center;gap:5px}
  .brand-dot{border-radius:50%;background:var(--berry);display:block}
  .brand-name{font-weight:700;color:var(--cocoa);white-space:nowrap}
  .brand-tag{color:var(--soft-ink);letter-spacing:.08em;text-transform:uppercase;margin-top:3px}
  .on-dark .brand-name{color:var(--paper)}
  .on-dark .brand-tag{color:#e8dccf}

  .piece{position:absolute;background:var(--paper);box-shadow:0 2px 6px rgba(60,40,20,.18);overflow:hidden}
  .wave{position:absolute;left:0;bottom:0;width:100%;display:block}

  /* business cards */
  .card{width:138px;height:72px}
  .card-front{left:30px;top:92px}
  .card-back{left:30px;top:230px;background:var(--cocoa);display:flex;align-items:center;justify-content:center}
  .card-back-alt{left:30px;top:324px;background:var(--cocoa);display:flex;align-items:center;padding-left:16px}
  .card-front .brand{position:absolute;left:10px;top:10px;align-items:flex-start}
  .card .brand-name{font-size:13px}
  .card .brand-dot{width:8px;height:8px}
  .card .brand-tag{font-size:4px}
  .card-person{position:absolute;right:10px;top:10px;text-align:right;font-size:5px;line-height:1.35}
  .card-person strong{display:block;font-size:6.5px;color:var(--cocoa)}

  /* letterheads */
  .letterhead{width:212px;height:384px;top:24px}
  .letterhead-a{left:222px}
  .letterhead-b{left:514px}
  .letterhead .brand{position:absolute;left:22px;top:22px;align-items:flex-start}
  .letterhead .brand-name{font-size:20px}
  .letterhead .brand-dot{width:11px;height:11px}
  .letterhead .brand-tag{font-size:5px}
  .letter-contact{position:absolute;font-size:5px;line-height:1.45;color:var(--soft-ink)}
  .letterhead-a .letter-contact{left:112px;top:24px}
  .letterhead-b .letter-contact{right:16px;bottom:56px;text-align:right;color:#f3e9de;z-index:2}

  /* envelopes */
  .envelopes{position:absolute;left:850px;top:22px;width:330px;height:390px}
  .envelopes .brand{position:absolute}
  .env-front-logo{left:118px;top:62px}
  .env-front-logo .brand-name{font-size:14px}
  .env-front-logo .brand-dot{width:8px;height:8px}
  .env-flap-logo{left:128px;top:120px}
  .env-flap-logo .brand-name{font-size:12px}
  .env-flap-logo .brand-dot{width:7px;height:7px}
</style>
</head>
<body>

  <!-- business cards -->
  <section class="piece card card-front">
    <div class="brand">
      <div class="brand-row"><span class="brand-dot"></span><span class="brand-name">Chill Bo</span></div>
      <span class="brand-tag">frozen yogurt and more</span>
    </div>
    <div class="card-person">
      <strong>Tara Kessler</strong>
      Owner<br>
      tarasglow@quillpost.com
    </div>
    <svg class="wave" viewBox="0 0 138 30" height="30" preserveAspectRatio="none" aria-hidden="true">
      <path d="M0 12 C40 2 80 26 138 8 L138 30 L0 30Z" fill="var(--lime)"/>
      <path d="M0 16 C40 6 80 30 138 12 L138 30 L0 30Z" fill="var(--cocoa)"/>
    </svg>
  </section>

  <section class="piece card card-back on-dark">
    <div class="brand">
      <div class="brand-row"><span class="brand-dot"></span><span class="brand-name">Chill Bo</span></div>
      <span class="brand-tag">frozen yogurt and more</span>
    </div>
  </section>

  <section class="piece card card-back-alt on-dark">
    <div class="brand" style="align-items:flex-start">
      <div class="brand-row"><span class="brand-dot"></span><span class="brand-name">Chill Bo</span></div>
      <span class="brand-tag">frozen yogurt and more</span>
    </div>
  </section>

  <!-- letterheads -->
  <section class="piece letterhead letterhead-a">
    <div class="brand">
      <div class="brand-row"><span class="brand-dot"></span><span class="brand-name">Chill Bo</span></div>
      <span class="brand-tag">frozen yogurt and more</span>
    </div>
    <address class="letter-contact" style="font-style:normal">
      4182 Larkspur Ln.<br>
      Columbus IN. 47358<br>
      tarasglow@quillpost.com
    </address>
    <svg class="wave" viewBox="0 0 212 60" height="60" preserveAspectRatio="none" aria-hidden="true">
      <path d="M0 24 C60 4 120 48 212 14 L212 60 L0 60Z" fill="var(--lime)"/>
      <path d="M0 30 C60 10 120 54 212 20 L212 60 L0 60Z" fill="var(--cocoa)"/>
    </svg>
  </section>

  <section class="piece letterhead letterhead-b">
    <div class="brand">
      <div class="brand-row"><span class="brand-dot"></span><span class="brand-name">Chill Bo</span></div>
      <span class="brand-tag">frozen yogurt and more</span>
    </div>
    <address class="letter-contact" style="font-style:normal">
      Tara Kessler, Owner<br>
      4182 Larkspur Ln. Columbus IN. 47358<br>
      tarasglow@quillpost.com
    </address>
    <svg class="wave" viewBox="0 0 212 70" height="70" preserveAspectRatio="none" aria-hidden="true">
      <path d="M0 22 C70 0 130 46 212 12 L212 70 L0 70Z" fill="var(--lime)"/>
      <path d="M0 28 C70 6 130 52 212 18 L212 70 L0 70Z" fill="var(--cocoa)"/>
    </svg>
  </section>

  <!-- envelopes -->
  <section class="envelopes">
    <svg width="330" height="390" viewBox="0 0 330 390" aria-hidden="true" style="position:absolute;left:0;top:0">
      <!-- envelope back, closed flap -->
      <rect x="8" y="0" width="314" height="96" fill="var(--paper)"/>
      <path d="M8 0 L165 58 L322 0Z" fill="#f6f2ec" stroke="var(--lime)" stroke-width="3"/>
      <!-- envelope back, brown flap open -->
      <rect x="8" y="148" width="314" height="96" fill="var(--paper)"/>
      <path d="M8 148 L165 96 L322 148Z" fill="var(--cocoa)"/>
      <path d="M8 148 L165 206 L322 148" fill="none" stroke="#e5ded4" stroke-width="1"/>
      <path d="M8 244 L150 180 M322 244 L180 180" stroke="#ece6dd" stroke-width="1"/>
      <!-- envelope back, white flap open -->
      <rect x="8" y="312" width="314" height="74" fill="var(--paper)"/>
      <path d="M8 312 L165 262 L322 312Z" fill="#f7f4ef" stroke="#e2dbd1" stroke-width="1"/>
      <path d="M8 386 L150 330 M322 386 L180 330" stroke="#ece6dd" stroke-width="1"/>
    </svg>
    <div class="brand env-front-logo">
      <div class="brand-row"><span class="brand-dot"></span><span class="brand-name">Chill Bo</span></div>
    </div>
    <div class="brand env-flap-logo on-dark">
      <div class="brand-row"><span class="brand-dot"></span><span class="brand-name">Chill Bo</span></div>
    </div>
  </section>

</body>
</html>
```